Brocure for Brindle - Social Media Management

Brindle is a Dutch company in the market of Social Media growth. We need a brochure (digital/PDF) for our company. Please see attached word doc for the text and attached logo. The initial proposal can contain just the first 4 pages text of the word doc.

We use informal language in all our communication.

Slogan: Effectieve Social Media Marketing voor professionals en ondernemers

Website: brindlesm-voorbeeld.nl

Industry/Entity Type

Digital Marketing

Contact Information for Business Card

Contact details:

Gerrit ter Hoeve
gerrit@brindlesm-voorbeeld.nl
06-19573826

```html
<!DOCTYPE html>
<html lang="nl">
<head>
<meta charset="utf-8">
<title>Brindle – Social Media Marketing brochure</title>
<link href="https://fonts.googleapis.com/css2?family=Barlow+Condensed:wght@500;600&family=Barlow:wght@400;500;600&display=swap" rel="stylesheet">
<style>
:root{
  --navy:#13254a;
  --navy-2:#1c3463;
  --orange:#f26a1b;
  --backdrop:#9c9da2;
  --paper:#ffffff;
  --ink:#2b2f3a;
  --text:#3b404c;
  --rule:#c9cfdb;
}
*{margin:0;padding:0;box-sizing:border-box}
html,body{width:1200px;height:453px;overflow:hidden;background:var(--backdrop)}
body{position:relative;font-family:'Barlow',sans-serif;color:var(--ink)}
.page{position:absolute;top:35px;width:262px;height:371px;background:var(--paper);overflow:hidden;box-shadow:0 2px 6px rgba(0,0,0,.25)}
.page--cover{left:28px}.page--intro{left:317px}.page--why{left:612px}.page--how{left:905px}
.abs{position:absolute}
.h-orange{font-family:'Barlow Condensed',sans-serif;font-weight:600;color:var(--orange);font-size:8.2px;letter-spacing:.2px;line-height:1}
.h-navy{font-family:'Barlow Condensed',sans-serif;font-weight:600;color:var(--navy);font-size:7px;line-height:1;display:flex;align-items:center;gap:3px}
.body{font-size:4.3px;line-height:1.3;text-align:justify;color:var(--text);font-weight:500}
.body p+p{margin-top:3.5px}
.on-navy{color:#eef1f6}
.brand{font-family:'Barlow',sans-serif;font-weight:600;color:var(--orange);letter-spacing:1px;display:flex;align-items:center;gap:3px;line-height:1}
.brand-dot{border-radius:50%;background:var(--orange);display:inline-block}
.tagline{font-family:'Barlow',sans-serif;font-weight:600;color:var(--navy);letter-spacing:.6px;line-height:1}
.footer{position:absolute;left:0;bottom:0;width:100%;height:17px;background:var(--navy);color:#fff;font-size:6px;display:flex;align-items:center;justify-content:center;gap:28px;letter-spacing:.4px}
.panel{position:absolute;background:var(--navy)}
.ico{width:9px;height:9px;flex:none}
/* cover */
.cover-title{left:0;width:100%;top:304px;text-align:center;font-family:'Barlow Condensed',sans-serif;font-weight:500;color:var(--navy);font-size:10.6px;line-height:1.15}
.cover-slogan{left:0;width:100%;top:337px;text-align:center;font-size:7.6px}
/* flow */
.flow{left:11px;top:62px;width:240px;height:50px}
.flow-box{position:absolute;top:17px;width:31px;height:31px;border:1px solid var(--navy);border-radius:4px;background:#fff;display:flex;align-items:center;justify-content:center}
.flow-box.alt{border-color:var(--orange)}
.flow-box svg{width:18px;height:18px}
.flow-num{position:absolute;top:-5px;right:-5px;width:9px;height:9px;border-radius:50%;background:var(--navy);color:#fff;font-size:5px;text-align:center;line-height:9px;font-weight:600}
.flow-box.alt .flow-num{background:var(--orange)}
.flow-formula{position:absolute;top:3px;left:0;width:100%;text-align:center;font-size:3.8px;font-weight:600;color:var(--navy)}
/* platform list */
.platforms{list-style:none;font-size:4.3px;color:#fff}
.platforms li{display:flex;align-items:center;gap:3px;height:10px}
.platforms li i{width:7px;height:7px;border:.7px solid #fff;border-radius:1.5px;display:inline-block}
/* steps */
.steps{left:12px;top:163px;width:240px}
.step{position:relative;padding-left:24px;margin-bottom:7px}
.step-dot{position:absolute;left:1px;top:0;width:15px;height:15px;border-radius:50%;background:var(--navy);border:1.5px solid var(--rule);display:flex;align-items:center;justify-content:center}
.step-dot svg{width:8px;height:8px}
.step-title{font-family:'Barlow Condensed',sans-serif;font-weight:600;font-size:5px;color:var(--navy);line-height:1.1}
.step .body{text-align:left;font-size:4.1px}
.step-line{position:absolute;left:20px;top:170px;width:.8px;height:160px;background:var(--rule)}
</style>
</head>
<body>

<!-- Page 1: cover -->
<section class="page page--cover">
  <svg class="abs" style="left:0;top:0" width="262" height="285" viewBox="0 0 262 285">
    <defs>
      <linearGradient id="cityfog" x1="0" y1="0" x2="1" y2="1">
        <stop offset="0" stop-color="#a9adb4"/><stop offset=".5" stop-color="#dcd9d4"/><stop offset="1" stop-color="#6f7176"/>
      </linearGradient>
      <radialGradient id="glow" cx=".28" cy=".5" r=".35">
        <stop offset="0" stop-color="#fff3e0"/><stop offset=".5" stop-color="#f4d9b6" stop-opacity=".6"/><stop offset="1" stop-color="#f4d9b6" stop-opacity="0"/>
      </radialGradient>
      <linearGradient id="floor" x1="0" y1="0" x2="0" y2="1"><stop offset="0" stop-color="#9a9a9c" stop-opacity="0"/><stop offset="1" stop-color="#4d4f54" stop-opacity=".7"/></linearGradient>
      <clipPath id="coverclip"><path d="M0 0H218C262 40 272 150 232 210C196 262 110 268 0 242Z"/></clipPath>
    </defs>
    <g clip-path="url(#coverclip)" role="img" aria-label="Foto: zakenvrouw kijkt naar een netwerk van verbonden profielpictogrammen">
      <rect width="262" height="285" fill="url(#cityfog)"/>
      <rect width="262" height="285" fill="url(#glow)"/>
      <rect y="170" width="262" height="100" fill="url(#floor)"/>
    </g>
    <path d="M218 0C262 40 272 150 232 210C196 262 110 268 0 242" fill="none" stroke="var(--orange)" stroke-width="3"/>
    <path d="M0 252C90 282 190 270 242 215" fill="none" stroke="var(--navy)" stroke-width="5"/>
  </svg>
  <div class="abs brand" style="left:74px;top:282px;font-size:15px"><span class="brand-dot" style="width:11px;height:11px"></span>BRINDLE</div>
  <div class="abs tagline" style="left:92px;top:295px;font-size:4.8px">SOCIAL MEDIA MARKETING</div>
  <h1 class="abs cover-title">SOCIAL MEDIA MARKETING VOOR ZAKELIJKE<br>PROFESSIONALS EN ONDERNEMERS</h1>
  <div class="abs cover-slogan h-orange">GROEI · INTERACTIE · EN CONTENT</div>
  <div class="abs" style="left:0;top:352px;width:100%;height:1px;background:var(--orange)"></div>
  <footer class="footer"><span>◎ www.brindlesm-voorbeeld.nl</span></footer>
</section>

<!-- Page 2: intro -->
<section class="page page--intro">
  <h2 class="abs h-orange" style="left:11px;top:22px">GROEI · INTERACTIE · EN CONTENT</h2>
  <div class="abs body" style="left:11px;top:33px;width:240px;text-align:left">Je bereik vergroten, traffic genereren en daarmee meer omzet behalen. Dat is wat wij bieden.<br>Onze services helpen jouw bereik op de sociale media te vergroten. Met een uitgekiende groeistrategie, onze kennis en geavanceerde tools zorgen we voor gerichte content en interactie op je sociale netwerken.</div>
  <div class="abs flow">
    <svg class="abs" style="left:0;top:0" width="240" height="50"><path d="M15 17V9H225V17" fill="none" stroke="var(--navy)" stroke-width=".8"/><line x1="31" y1="32" x2="209" y2="32" stroke="var(--navy)" stroke-width=".8"/></svg>
    <div class="flow-formula">((ACTIEVE INTERACTIE + RELEVANTE CONTENT) &gt; ACTIEVE VOLGERS) = (&gt; TRAFFIC + OMZET)</div>
    <div class="flow-box" style="left:0"><span class="flow-num">1</span>
      <svg viewBox="0 0 20 20"><circle cx="10" cy="10" r="7" fill="none" stroke="var(--navy)" stroke-width="1.4"/><path d="M6.5 10.2l2.4 2.4 4.6-5" fill="none" stroke="var(--navy)" stroke-width="1.6"/></svg></div>
    <div class="flow-box alt" style="left:52px"><span class="flow-num">2</span>
      <svg viewBox="0 0 20 20"><rect x="4" y="2.5" width="12" height="15" rx="1" fill="none" stroke="var(--orange)" stroke-width="1.3"/><path d="M6.5 7h7M6.5 10h7M6.5 13h4" stroke="var(--orange)" stroke-width="1.2"/></svg></div>
    <div class="flow-box" style="left:104px"><span class="flow-num">3</span>
      <svg viewBox="0 0 20 20"><rect x="3" y="12" width="3" height="5" fill="var(--navy)"/><rect x="8.5" y="8" width="3" height="9" fill="var(--navy)"/><rect x="14" y="4" width="3" height="13" fill="var(--navy)"/></svg></div>
    <div class="flow-box alt" style="left:156px"><span class="flow-num">4</span>
      <svg viewBox="0 0 20 20"><circle cx="10" cy="11" r="6.5" fill="none" stroke="var(--orange)" stroke-width="1.3"/><path d="M10 7.5V11l2.5 2M8 2.5h4" fill="none" stroke="var(--orange)" stroke-width="1.3"/></svg></div>
    <div class="flow-box" style="left:208px"><span class="flow-num">5</span>
      <svg viewBox="0 0 20 20"><rect x="2.5" y="4" width="15" height="10" rx="1" fill="none" stroke="var(--navy)" stroke-width="1.3"/><path d="M7 17h6M10 14v3" stroke="var(--navy)" stroke-width="1.3"/><path d="M6 11l3-3 2 2 3-3" fill="none" stroke="var(--navy)" stroke-width="1.2"/></svg></div>
  </div>
  <h3 class="abs h-navy" style="left:11px;top:126px">WIE ZIJN WIJ?</h3>
  <div class="abs body" style="left:11px;top:136px;width:117px">Wij zijn Brindle. Een team van sociale media experts dat je sociale netwerk activeert en het bereik vergroot. We zorgen voor sociale interactie met volgers, nieuwe en bestaande. Daarmee genereren we traffic naar je website/shop. Het doel? Meer omzet. Simpel en heel meetbaar.</div>
  <h3 class="abs h-navy" style="left:11px;top:180px">VOOR WIE?</h3>
  <div class="abs body" style="left:11px;top:190px;width:117px">Onze dienstverlening kan ingezet worden op zowel persoonlijke zakelijke profielen, of voor bedrijfspagina's op diverse sociale mediakanalen.</div>
  <h3 class="abs h-navy" style="left:135px;top:126px">WAT DOEN WE?</h3>
  <div class="abs body" style="left:135px;top:136px;width:117px">
    <p>Samen met jou bepalen we je doelen in de sociale netwerken. Zowel strategisch als tactisch en operationeel. Wij richten ons op die doelen en zorgen voor een netwerk van echte en actieve volgers.</p>
    <p>Of het nu gaat om zakelijke netwerken of fotokanalen, interactie zorgt voor betrokken volgers. Die jij vervolgens in je verkoopproces kunt oppakken.</p>
    <p>Voor zakelijke professionals verzorgen wij personal branding met als doel impact en social sales. We zorgen voor meer relevante connecties en activeren je netwerk. Gecombineerd met de juiste contentstrategie zorgen wij ervoor dat je gezien wordt als autoriteit.</p>
    <p>Onze diensten voor bedrijven bestaan uit de versnelde organische groei van het volgernetwerk en het activeren van het netwerk met content en interactie. Zo zorgen we voor bereik en verkeer naar je website.</p>
  </div>
  <div class="panel" style="left:0;top:248px;width:262px;height:123px"></div>
  <svg class="abs" style="left:0;top:228px" width="140" height="143" viewBox="0 0 140 143">
    <defs>
      <linearGradient id="phoneuser" x1="0" y1="0" x2="1" y2="1"><stop offset="0" stop-color="#d6b79a"/><stop offset=".45" stop-color="#9a6742"/><stop offset="1" stop-color="#3a2a24"/></linearGradient>
      <radialGradient id="phonelight" cx=".3" cy=".3" r=".5"><stop offset="0" stop-color="#f3e4d2" stop-opacity=".8"/><stop offset="1" stop-color="#f3e4d2" stop-opacity="0"/></radialGradient>
    </defs>
    <path d="M0 7C60 0 118 40 135 143H0Z" fill="var(--orange)"/>
    <g role="img" aria-label="Foto: lachende vrouw met een smartphone in haar hand">
      <path d="M0 11C58 5 112 44 128 143H0Z" fill="url(#phoneuser)"/>
      <path d="M0 11C58 5 112 44 128 143H0Z" fill="url(#phonelight)"/>
    </g>
  </svg>
  <h3 class="abs h-orange" style="left:143px;top:263px;font-size:8px">WELKE PLATFORMEN?</h3>
  <div class="abs" style="left:143px;top:274px;font-size:4px;color:var(--orange)">We bieden onze diensten aan op alle belangrijke platformen:</div>
  <ul class="abs platforms" style="left:143px;top:281px">
    <li><i></i>Netwerkr (bedrijfspagina's en persoonlijke profielen)</li>
    <li><i></i>Kringboek (bedrijfspagina's en groepen)</li>
    <li><i></i>Fotogram (bedrijfspagina's en persoonlijke profielen)</li>
    <li><i></i>Kwetter</li>
    <li><i></i>KijkBuis</li>
    <li><i></i>Zoekr Bedrijfsprofiel</li>
    <li><i></i>Optioneel: Klikklak, Prikbord, Fora en Blogr</li>
  </ul>
</section>

<!-- Page 3: why -->
<section class="page page--why">
  <svg class="abs" style="left:0;top:0" width="262" height="106" viewBox="0 0 262 106">
    <defs>
      <linearGradient id="teamoffice" x1="0" y1="0" x2="1" y2="0"><stop offset="0" stop-color="#eef1f4"/><stop offset=".35" stop-color="#c7d0da"/><stop offset=".6" stop-color="#6f6459"/><stop offset=".8" stop-color="#a49282"/><stop offset="1" stop-color="#d7dde3"/></linearGradient>
      <radialGradient id="teamwarm" cx=".62" cy=".4" r=".35"><stop offset="0" stop-color="#c89a78" stop-opacity=".7"/><stop offset="1" stop-color="#c89a78" stop-opacity="0"/></radialGradient>
    </defs>
    <g role="img" aria-label="Foto: team viert succes met een high five rond een vergadertafel">
      <path d="M0 0H262V66C262 90 248 104 224 104H0Z" fill="url(#teamoffice)"/>
      <path d="M0 0H262V66C262 90 248 104 224 104H0Z" fill="url(#teamwarm)"/>
    </g>
  </svg>
  <div class="abs brand" style="left:12px;top:48px;font-size:12px"><span class="brand-dot" style="width:9px;height:9px"></span>BRINDLE</div>
  <div class="abs tagline" style="left:24px;top:61px;font-size:3.8px;color:var(--navy)">SOCIAL MEDIA MARKETING</div>
  <h3 class="abs h-navy" style="left:10px;top:125px"><svg class="ico" viewBox="0 0 10 10"><circle cx="5" cy="5" r="4.2" fill="none" stroke="var(--orange)" stroke-width="1"/><circle cx="5" cy="5" r="1.6" fill="var(--navy)"/></svg>WAAROM KIES JE VOOR ONS?</h3>
  <div class="abs body" style="left:10px;top:136px;width:121px">
    <p>Jij hebt jouw vak, wij het onze. Als iedereen doet waar hij goed in is, worden daar allemaal beter van. Wij zijn goed in het activeren en vergroten van je sociale netwerk. Daarvoor gebruiken we een slimme mix van kennis en tools.</p>
    <p>Een strategie die ervoor zorgt dat jij je kunt focussen op je corebusiness. Met onze slimme tools vergroten wij de impact van je sociale netwerken. Met als resultaat: meer traffic, meer leads, meer omzet.</p>
  </div>
  <h3 class="abs h-navy" style="left:10px;top:194px"><svg class="ico" viewBox="0 0 10 10"><circle cx="5" cy="5" r="2.6" fill="none" stroke="var(--orange)" stroke-width="1.6" stroke-dasharray="1.6 .8"/><circle cx="5" cy="5" r="1" fill="var(--navy)"/></svg>DOEN WE ALLES ZELF?</h3>
  <div class="abs body" style="left:10px;top:205px;width:121px">Wij zijn slim in de strategie en systemen voor het vergroten van interactie. En we hebben een netwerk van specialisten die slim zijn in hun vak. Zoals een reclamebureau, creatief ontwerper, websitebouwer of marketingstrategiebureau. Is er op dat vlak een behoefte, dan brengen wij je graag in contact.</div>
  <h3 class="abs h-navy" style="left:134px;top:125px"><svg class="ico" viewBox="0 0 10 10"><circle cx="3" cy="3.5" r="1.6" fill="var(--orange)"/><circle cx="7" cy="3.5" r="1.6" fill="var(--orange)"/><path d="M0.5 9c0-2.5 5-2.5 5 0M4.5 9c0-2.5 5-2.5 5 0" fill="var(--navy)"/></svg>VOLLEDIG SOCIAAL MANAGEMENT</h3>
  <div class="abs body" style="left:134px;top:136px;width:120px">We bieden een compleet beheerpakket voor sociale media waarmee we betrokkenheid van volgers realiseren en tijdig en altijd proactief schakelen naar de volgende stap. Zo blijven bezoekers geboeid en actief. We plannen zowel doelgroep- als branche specifieke inhoud en combineren online aanwezigheid om meer en meer gericht websiteverkeer te genereren.</div>
  <h3 class="abs h-navy" style="left:134px;top:182px"><svg class="ico" viewBox="0 0 10 10"><circle cx="5" cy="5" r="4.2" fill="none" stroke="var(--orange)" stroke-width="1"/><path d="M1 5h8M5 1c-2 2.5-2 5.5 0 8M5 1c2 2.5 2 5.5 0 8" fill="none" stroke="var(--orange)" stroke-width=".7"/></svg>ACTIVEREN VAN JE NETWERK</h3>
  <div class="abs body" style="left:134px;top:193px;width:120px">
    <p>Je bent al een poos bezig met het beheren van je sociale media, maar ziet geen commercieel resultaat? De specialist maakt het verschil. Jouw kennis van jouw product en klant, gecombineerd met ons specialisme over sociale media. In zeer diverse branches.</p>
    <p>Wij gebruiken deze kennis voor een contentstrategie op maat. Een strategie die gegarandeerd meer likes, retweets en doorklikken genereert. Meer likes, meer interactie, meer betrokkenheid: meer omzet.</p>
  </div>
  <div class="panel" style="left:0;top:248px;width:262px;height:123px"></div>
  <h3 class="abs h-orange" style="left:8px;top:262px;font-size:7px;display:flex;align-items:center;gap:3px"><svg class="ico" viewBox="0 0 10 10"><rect x="0.5" y="6" width="2" height="3.5" fill="var(--orange)"/><rect x="3.5" y="4" width="2" height="5.5" fill="var(--orange)"/><rect x="6.5" y="2" width="2" height="7.5" fill="var(--orange)"/></svg>GROEIEN OP SOCIALE MEDIA</h3>
  <div class="abs body on-navy" style="left:8px;top:274px;width:123px">
    <p>Het staat als een paal boven water: sociale media zijn een krachtig marketinginstrument. Een kans die je niet voorbij kunt laten gaan, of je dat nu leuk vindt of niet. Het geeft je de kans om je merk op te bouwen, je zicht- en vindbaarheid te verbeteren en uiteindelijk meer leads en verkopen te genereren.</p>
    <p>Het beheren van je sociale platforms is een tijdrovende klus. En om resultaat te krijgen, moet je het ook nog eens slim doen. Om de online herkenbaarheid van je bedrijf te vergroten, zijn je uitingen de sleutel.</p>
    <p>Interactie, consistentie, responsiveness, allemaal zorgen ze voor herkenning en betrokkenheid van je volgers. We helpen je om je digitale activiteiten te verbinden en je bedrijf te laten groeien.</p>
  </div>
  <h3 class="abs h-orange" style="left:134px;top:262px;font-size:7px;display:flex;align-items:center;gap:3px"><svg class="ico" viewBox="0 0 10 10"><path d="M1 8l3-3 2 2 3-4" fill="none" stroke="var(--orange)" stroke-width="1.2"/><path d="M7 3h2v2" fill="none" stroke="var(--orange)" stroke-width="1.2"/></svg>GROEISTRATEGIE</h3>
  <div class="abs body on-navy" style="left:134px;top:274px;width:120px">
    <p>Je netwerk op sociale media laten groeien kan een lastige klus zijn. Maar het levert je enorm veel op. Een groot aantal echte en actieve volgers geeft vertrouwen en genereert nog meer betrokkenheid.</p>
    <p>Het is de moderne variant van mond-tot-mondreclame.</p>
    <p>Wij hebben de expertise en oplossingen om al je profielen een echte boost te geven. Met onze tools krijgen we de volledige controle over je kanalen, zodat jij jouw focus kunt richten op de uitvoering en levering van opdrachten.</p>
    <p>En wees voorbereid op groei!</p>
  </div>
</section>

<!-- Page 4: how -->
<section class="page page--how">
  <svg class="abs" style="left:0;top:0" width="262" height="116" viewBox="0 0 262 116">
    <defs>
      <linearGradient id="woodtable" x1="0" y1="0" x2="1" y2="1"><stop offset="0" stop-color="#4a3424"/><stop offset=".45" stop-color="#9c7452"/><stop offset="1" stop-color="#5a3d28"/></linearGradient>
      <radialGradient id="woodlight" cx=".55" cy=".45" r=".4"><stop offset="0" stop-color="#e9dccd" stop-opacity=".55"/><stop offset="1" stop-color="#e9dccd" stop-opacity="0"/></radialGradient>
    </defs>
    <g role="img" aria-label="Foto: team aan een houten tafel met laptops en een woordwolk rond marketing">
      <path d="M0 0H262V114H28C12 114 0 102 0 86Z" fill="url(#woodtable)"/>
      <path d="M0 0H262V114H28C12 114 0 102 0 86Z" fill="url(#woodlight)"/>
    </g>
  </svg>
  <div class="abs brand" style="left:76px;top:124px;font-size:15px"><span class="brand-dot" style="width:11px;height:11px"></span>BRINDLE</div>
  <div class="abs tagline" style="left:92px;top:137px;font-size:4.8px">SOCIAL MEDIA MARKETING</div>
  <h2 class="abs h-orange" style="left:12px;top:151px">HOE WERKT HET?</h2>
  <div class="step-line"></div>
  <div class="abs steps">
    <div class="step"><span class="step-dot"><svg viewBox="0 0 10 10"><circle cx="4.2" cy="4.2" r="2.8" fill="none" stroke="#fff" stroke-width="1.1"/><path d="M6.3 6.3L9 9" stroke="#fff" stroke-width="1.2"/></svg></span><div class="step-title">QUICK SCAN &amp; ADVIES</div><div class="body">We starten altijd met een grondige analyse van je website en sociale kanalen. Op basis daarvan geven we je een advies over de beste strategie.</div></div>
    <div class="step"><span class="step-dot"><svg viewBox="0 0 10 10"><path d="M2 5.2l2 2 4-4.5" fill="none" stroke="#fff" stroke-width="1.3"/></svg></span><div class="step-title">JE WILT MET ONS IN ZEE</div><div class="body"><p>Als je besluit met ons in zee te gaan, doen we dat niet voor een paar weken. Want we doen niet aan hit-and-run, maar bouwen aan samenwerking die op de lange termijn echte resultaten oplevert. We moeten elkaar goed leren kennen en dat vraagt tijd.</p><p>Je vertrouwt ons je sociale mediakanalen toe. Dat vraagt vertrouwen en tegelijk moeten wij ons goed inleven in de manier van communicatie die past bij jouw business en jouw doelgroep. Van beide kanten vraagt dit een tijdsinvestering.</p></div></div>
    <div class="step"><span class="step-dot"><svg viewBox="0 0 10 10"><rect x="1.5" y="2" width="7" height="6.5" fill="none" stroke="#fff" stroke-width="1"/><path d="M3 4.2h4M3 6.2h4" stroke="#fff" stroke-width=".8"/></svg></span><div class="step-title">PAKKETKEUZE</div><div class="body">We hebben verschillende servicepakketten waaruit je kunt kiezen wat bij jouw situatie en wensen past. Blijkt op basis van de QuickScan dat je beter af bent met maatwerk, dan maken we daarover specifieke afspraken. Geen twee klanten zijn gelijk, daarom is ons aanbod flexibel opgebouwd.</div></div>
    <div class="step"><span class="step-dot"><svg viewBox="0 0 10 10"><path d="M1.5 8.5l6-6M4.5 2.5h3v3" fill="none" stroke="#fff" stroke-width="1.2"/></svg></span><div class="step-title">IMPLEMENTATIE</div><div class="body"><p>Natuurlijk wil je zo snel mogelijk resultaat zien. Dat willen wij ook. We werken de strategie uit in een plan en gaan voor jou aan het werk. Met de prioriteit op die gebieden die zo snel mogelijk resultaten opleveren. Omdat we graag (laten) zien dat onze inspanningen verschil maken.</p><p>We richten daarvoor de benodigde systemen in. In het begin hebben we regelmatig overleg om elkaar goed te leren kennen en de vinger aan de pols te houden.</p></div></div>
    <div class="step"><span class="step-dot"><svg viewBox="0 0 10 10"><path d="M8 4A3.2 3.2 0 1 0 8.2 6.5" fill="none" stroke="#fff" stroke-width="1.1"/><path d="M8.6 1.6V4.3H5.9" fill="none" stroke="#fff" stroke-width="1.1"/></svg></span><div class="step-title">TERUGKOPPELING EN VERBETERING</div><div class="body">Iedere ondernemer is gedreven als het gaat om het behalen van resultaten. Zo ook wij. Wij doen er alles aan om onze dienstverlening zo succesvol mogelijk te laten zijn en jouw sociale doelen te behalen. We hebben regelmatig contact om de resultaten te bespreken en daar waar mogelijk te verbeteren.</div></div>
  </div>
  <footer class="footer" style="font-size:5.4px;gap:18px"><span>✉ gerrit@brindlesm-voorbeeld.nl</span><span>✆ 06-19573826</span><span>www.brindlesm-voorbeeld.nl</span></footer>
</section>

</body>
</html>
```